Marketing Collateral for Construction Company
Keystone Cellar Craftworks
Attention Designers:
I have uploaded a number of pictures of basement project that our company has done. Please use these pictures where you think they will work in the designs for the marketing peripherals.
Thank you,
Mark
where is the content for the flyer and brochure?
@QW - please check your private messages on top right corner once you login to your account & reply. Thanks
Designers,
I have changed the scope of the project only to include:
-tri-fold brochure
-flyer
-door hanger
I have also uploaded AI files for you to use in your designs. Please let me know if you need more source files or a different format.
Thanks,

```html
<!DOCTYPE html>
<html lang="en">
<head>
<meta charset="utf-8">
<title>Keystone Cellar Craftworks – Marketing Collateral</title>
<link rel="stylesheet" href="https://fonts.googleapis.com/css2?family=Open+Sans:wght@400;600;700&display=swap">
<style>
  :root{
    --backdrop:#2b2521;
    --green-dark:#2f7d1f;
    --green:#4aa62a;
    --green-light:#8cc63f;
    --blue:#1f4aa0;
    --blue-light:#3c6fc4;
    --paper:#ffffff;
    --ink:#3a3a3a;
    --placeholder:#9a9a9a;
    --label:#ffffff;
  }
  *{box-sizing:border-box;margin:0;padding:0}
  html,body{width:1200px;height:874px;overflow:hidden}
  body{background:var(--backdrop);font-family:"Open Sans",Arial,sans-serif;position:relative}
  .section-label{position:absolute;color:var(--label);font-weight:600;font-size:30px;letter-spacing:.2px}
  .piece{position:absolute;background:var(--paper);overflow:hidden}
  .piece svg.art{position:absolute;inset:0;width:100%;height:100%}
  .abs{position:absolute}
  .heading{font-weight:700;font-size:11px;color:var(--paper)}
  .heading.dark{color:var(--green-dark)}
  .copy{font-size:5.4px;line-height:1.45;color:var(--paper)}
  .copy.dark{color:var(--ink)}
  .copy p+p{margin-top:4px}
  .photo-slot{display:flex;align-items:center;justify-content:center;text-align:center;font-size:12px;line-height:1.25;color:var(--placeholder);background:var(--paper);border:1px solid #ddd}
  .photo-slot.grey{background:var(--placeholder);color:var(--paper);border:none}
  .photo-slot.bare{background:none;border:none;color:var(--paper);justify-content:flex-start;text-align:left}
  .brand{display:flex;align-items:center;gap:5px}
  .brand .dot{width:10px;height:10px;border-radius:50%;background:var(--green)}
  .brand .name{font-weight:700;color:var(--green-dark);line-height:1.05;white-space:nowrap}
  .tagline{font-size:6px;color:var(--ink);white-space:nowrap}
  .web{font-size:5.5px;color:var(--paper);white-space:nowrap}
</style>
</head>
<body>

<div class="section-label" style="left:168px;top:66px">Brochure</div>
<div class="section-label" style="left:595px;top:66px">Flyer</div>
<div class="section-label" style="left:950px;top:296px">Door Hanger</div>

<section class="piece brochure-outside" style="left:43px;top:144px;width:427px;height:312px">
  <svg class="art" viewBox="0 0 427 312" preserveAspectRatio="none" aria-hidden="true">
    <defs>
      <linearGradient id="gA" x1="0" y1="0" x2="1" y2="1">
        <stop offset="0" stop-color="#3f9a22"/><stop offset="1" stop-color="#7fc23a"/>
      </linearGradient>
    </defs>
    <path d="M0 0H122C152 80 152 200 112 312H0Z" fill="url(#gA)"/>
    <path d="M0 232C55 258 95 282 122 312H0Z" fill="var(--blue)"/>
    <path d="M122 0C152 80 152 200 112 312" fill="none" stroke="#c9c9c9" stroke-width="4"/>
    <path d="M112 312C150 210 220 150 300 150C360 150 400 185 427 220V312Z" fill="url(#gA)"/>
    <path d="M112 312C150 210 220 150 300 150C360 150 400 185 427 220" fill="none" stroke="#cfcfcf" stroke-width="3"/>
    <path d="M300 312C350 290 395 270 427 250V312Z" fill="var(--blue)"/>
  </svg>
  <div class="abs brand" style="left:8px;top:10px"><span class="dot" style="width:7px;height:7px"></span><span class="name" style="font-size:5px;color:#fff">Keystone Cellar<br>Craftworks</span></div>
  <div class="abs heading" style="left:18px;top:28px">About Us</div>
  <div class="abs copy" style="left:12px;top:46px;width:108px">
    <p>We turn unfinished basements into warm, useful living space. Our crew plans every wall, light and outlet with care, so each room fits the way your family lives. From framing to final trim, we handle the whole build with clear pricing and steady communication.</p>
  </div>
  <div class="abs photo-slot bare" style="left:10px;top:258px;width:80px;height:34px">Place photo<br>HERE</div>
  <div class="abs photo-slot" style="left:165px;top:36px;width:110px;height:94px">Place photo<br>HERE</div>
  <div class="abs copy" style="left:180px;top:206px;width:90px">
    <p>Call today for a free in-home design visit and estimate.</p>
  </div>
  <div class="abs brand" style="left:300px;top:32px"><span class="dot"></span><span class="name" style="font-size:10px">Keystone Cellar<br>Craftworks</span></div>
  <div class="abs tagline" style="left:316px;top:66px">Spaces Built to Live In</div>
  <div class="abs photo-slot grey" style="left:298px;top:132px;width:115px;height:96px">Place photo<br>HERE</div>
</section>

<section class="piece brochure-inside" style="left:43px;top:487px;width:427px;height:312px">
  <svg class="art" viewBox="0 0 427 312" preserveAspectRatio="none" aria-hidden="true">
    <defs>
      <linearGradient id="gB" x1="0" y1="0" x2="1" y2="1">
        <stop offset="0" stop-color="#7fc23a"/><stop offset="1" stop-color="#338a20"/>
      </linearGradient>
    </defs>
    <path d="M150 312C128 200 140 80 196 0H427V312Z" fill="url(#gB)"/>
    <path d="M150 312C128 200 140 80 196 0" fill="none" stroke="#cfcfcf" stroke-width="4"/>
    <path d="M300 312C350 292 395 262 427 232V312Z" fill="var(--blue)"/>
  </svg>
  <div class="abs brand" style="left:8px;top:10px"><span class="dot" style="width:7px;height:7px"></span><span class="name" style="font-size:5px">Keystone Cellar<br>Craftworks</span></div>
  <div class="abs heading dark" style="left:18px;top:26px">About Us</div>
  <div class="abs copy dark" style="left:12px;top:44px;width:118px">
    <p>We turn unfinished basements into warm, useful living space. Our crew plans every wall, light and outlet with care, so each room fits the way your family lives. From framing to final trim, we handle the whole build with clear pricing and steady communication.</p>
  </div>
  <div class="abs photo-slot grey" style="left:8px;top:161px;width:108px;height:84px">Place photo<br>HERE</div>
  <div class="abs copy" style="left:160px;top:150px;width:112px">
    <p>We turn unfinished basements into warm, useful living space. Our crew plans every wall, light and outlet with care, so each room fits the way your family lives. From framing to final trim, we handle the whole build with clear pricing and steady communication.</p>
    <p>Home theaters, guest suites, wet bars, gyms and offices built to last.</p>
  </div>
  <div class="abs photo-slot bare" style="left:332px;top:262px;width:80px;height:34px">Place photo<br>HERE</div>
</section>

<section class="piece flyer" style="left:492px;top:149px;width:312px;height:403px">
  <svg class="art" viewBox="0 0 312 403" preserveAspectRatio="none" aria-hidden="true">
    <defs>
      <linearGradient id="gC" x1="0" y1="0" x2="1" y2="1">
        <stop offset="0" stop-color="#7fc23a"/><stop offset="1" stop-color="#2f7d1f"/>
      </linearGradient>
    </defs>
    <path d="M0 0H92C132 100 142 200 132 310C200 330 260 340 312 330V403H0Z" fill="url(#gC)"/>
    <path d="M92 0C132 100 142 200 132 310C200 330 260 340 312 330" fill="none" stroke="var(--blue-light)" stroke-width="3"/>
    <path d="M100 0C140 100 150 200 140 302" fill="none" stroke="#d0d0d0" stroke-width="3"/>
  </svg>
  <div class="abs brand" style="left:150px;top:40px"><span class="dot" style="width:12px;height:12px"></span><span class="name" style="font-size:14px">Keystone Cellar<br>Craftworks</span></div>
  <div class="abs tagline" style="left:186px;top:80px">Spaces Built to Live In</div>
  <div class="abs photo-slot grey" style="left:156px;top:151px;width:144px;height:96px">Place photo<br>HERE</div>
  <div class="abs copy" style="left:12px;top:128px;width:110px">
    <p>We turn unfinished basements into warm, useful living space. Our crew plans every wall, light and outlet with care, so each room fits the way your family lives. From framing to final trim, we handle the whole build with clear pricing and steady communication.</p>
  </div>
  <div class="abs copy dark" style="left:152px;top:258px;width:148px">
    <p>Home theaters, guest suites, wet bars, gyms and offices built to last. Call today for a free in-home design visit and estimate.</p>
  </div>
  <div class="abs web" style="left:220px;top:385px">www.keystonecellarcraft.com</div>
</section>

<section class="piece door-hanger-front" style="left:869px;top:511px;width:115px;height:317px">
  <svg class="art" viewBox="0 0 115 317" preserveAspectRatio="none" aria-hidden="true">
    <defs>
      <linearGradient id="gD" x1="0" y1="0" x2="1" y2="1">
        <stop offset="0" stop-color="#7fc23a"/><stop offset="1" stop-color="#2f7d1f"/>
      </linearGradient>
    </defs>
    <path d="M0 215C40 200 80 190 115 200V317H0Z" fill="url(#gD)"/>
    <path d="M0 215C40 200 80 190 115 200" fill="none" stroke="#cfcfcf" stroke-width="3"/>
    <circle cx="57" cy="48" r="20" fill="var(--backdrop)"/>
    <rect x="55" y="0" width="4" height="30" fill="var(--backdrop)"/>
  </svg>
  <div class="abs brand" style="left:8px;top:118px"><span class="dot" style="width:8px;height:8px"></span><span class="name" style="font-size:9px">Keystone Cellar<br>Craftworks</span></div>
  <div class="abs tagline" style="left:18px;top:146px;font-size:5.5px">Spaces Built to Live In</div>
</section>

<section class="piece door-hanger-back" style="left:996px;top:511px;width:115px;height:317px">
  <svg class="art" viewBox="0 0 115 317" preserveAspectRatio="none" aria-hidden="true">
    <defs>
      <linearGradient id="gE" x1="0" y1="0" x2="1" y2="1">
        <stop offset="0" stop-color="#8cc63f"/><stop offset="1" stop-color="#2f7d1f"/>
      </linearGradient>
    </defs>
    <rect width="115" height="317" fill="url(#gE)"/>
    <path d="M0 190C40 178 80 172 115 182" fill="none" stroke="#d6d6d6" stroke-width="2"/>
    <circle cx="57" cy="48" r="20" fill="var(--backdrop)"/>
    <rect x="55" y="0" width="4" height="30" fill="var(--backdrop)"/>
  </svg>
  <div class="abs photo-slot" style="left:14px;top:96px;width:86px;height:84px;font-size:10px">Place photo<br>HERE</div>
  <div class="abs heading" style="left:8px;top:216px;font-size:8px">About Us</div>
  <div class="abs copy" style="left:8px;top:230px;width:100px;font-size:4.6px">
    <p>We turn unfinished basements into warm, useful living space. Our crew plans every wall, light and outlet with care, so each room fits the way your family lives. From framing to final trim, we handle the whole build with clear pricing and steady communication.</p>
  </div>
  <div class="abs web" style="left:22px;top:302px;font-size:5px">www.keystonecellarcraft.com</div>
</section>

</body>
</html>
```